Software allocation system needs a business card design

We need a business card designed for our software platform - www.tolvexa.com.au

At the moment the logo and website is all black and white, we are happy for suggestions on implementing some colour throughout either the logo or business card.

Industry/Entity Type

Software

Font styles to use
Sans Serif

Colors

Designer to choose colors to be used in the design.

```html
<!DOCTYPE html>
<html lang="en">
<head>
<meta charset="utf-8">
<title>Tolvexa business cards</title>
<link rel="stylesheet" href="https://fonts.googleapis.com/css2?family=Raleway:wght@300;400&display=swap">
<style>
  :root {
    --backdrop: #e6e6e4;
    --card: #f4f4f3;
    --ink: #222222;
    --ink-soft: #4a4a4a;
    --accent: #1a9fc9;
    --shadow: rgba(0, 0, 0, 0.14);
  }
  * { box-sizing: border-box; margin: 0; padding: 0; }
  html, body {
    width: 1200px;
    height: 900px;
    overflow: hidden;
    background: var(--backdrop);
    font-family: "Raleway", "Helvetica Neue", Arial, sans-serif;
    color: var(--ink);
  }
  .canvas {
    position: relative;
    width: 1200px;
    height: 900px;
  }
  .card {
    position: absolute;
    top: 300px;
    width: 525px;
    height: 300px;
    overflow: hidden;
    background: var(--card);
    box-shadow: 0 6px 18px var(--shadow);
  }
  .card--back { left: 50px; }
  .card--front { left: 625px; }

  /* back face */
  .back-disc {
    position: absolute;
    left: -70px;
    top: 30px;
    width: 270px;
    height: 270px;
    border-radius: 50%;
    background: var(--ink);
  }
  .back-name {
    position: absolute;
    left: 232px;
    top: 96px;
    font-weight: 300;
    font-size: 34px;
    letter-spacing: 0.14em;
    color: var(--ink);
  }
  .back-url {
    position: absolute;
    right: 30px;
    top: 176px;
    font-weight: 300;
    font-size: 15px;
    letter-spacing: 0.04em;
    color: var(--accent);
  }

  /* front face */
  .marker {
    position: absolute;
    left: 26px;
    top: 66px;
  }
  .details {
    position: absolute;
    left: 70px;
    top: 52px;
    font-weight: 300;
    font-size: 13px;
    line-height: 1.35;
    color: var(--ink-soft);
  }
  .person {
    font-size: 21px;
    letter-spacing: 0.02em;
    color: var(--ink);
    margin-bottom: 6px;
  }
  .person__role {
    font-size: 13px;
    letter-spacing: 0.08em;
    margin-left: 4px;
  }
  .label { color: var(--accent); font-size: 14px; letter-spacing: 0.04em; }
  .contact-row { font-size: 14px; }
  .address { margin-top: 12px; font-size: 14px; color: var(--ink); }
  .web { margin-top: 10px; font-size: 14px; color: var(--accent); }
  .front-brand {
    position: absolute;
    left: 70px;
    bottom: 28px;
    display: flex;
    align-items: center;
    gap: 10px;
    font-weight: 300;
    font-size: 34px;
    letter-spacing: 0.14em;
    color: var(--ink);
  }
  .front-brand__dot {
    width: 18px;
    height: 18px;
    border-radius: 50%;
    background: var(--ink);
  }
</style>
</head>
<body>
<main class="canvas">
  <section class="card card--back" aria-label="Card back">
    <span class="back-disc" aria-hidden="true"></span>
    <p class="back-name">TOLVEXA</p>
    <p class="back-url">www.tolvexa.com.au</p>
  </section>

  <section class="card card--front" aria-label="Card front">
    <svg class="marker" width="22" height="20" viewBox="0 0 22 20" aria-hidden="true">
      <polygon points="0,0 22,10 0,20" fill="var(--accent)"/>
    </svg>
    <div class="details">
      <p class="person">DARA WENSLEY <span class="person__role">| MANAGER</span></p>
      <p class="contact-row"><span class="label">PHONE</span> 555.210.4836 &nbsp;<span class="label">FAX</span> 555.210.4871</p>
      <p class="contact-row"><span class="label">EMAIL</span> &nbsp;dwensley@tolvexa.com.au</p>
      <p class="address">PO Box 812<br>Harbourside NSW 2071</p>
      <p class="web">www.tolvexa.com.au</p>
    </div>
    <div class="front-brand"><span class="front-brand__dot"></span>TOLVEXA</div>
  </section>
</main>
</body>
</html>
```